Stationary KV Relay
business card, letterhead, envelopes, email signature,memo pad and invoice/quotes
Project: Stationary KV Relay
Stationary KV Relay   - Telecommunications
Creative Brief
Use same font as used in my logo
or any
Bright & Fun-filled
Tom Variscoff
CEO
3F B28 GALERI NUSAPARK JAKARTA PUSAT 14071
tom@kvrelay.com
www.kvrelay.com
Feel free to utilize different styles but try to stick to the company logo colors as best as possible.
Require: Business card, Stationary, Envelopes, Invoice, E-mail signature & Notepad
pwarnet pwarnet
EPS format upload already
brightoak brightoak
definitely!! but there is lots of designs please rate my design so i will easy to make the stationary of your like designs thanks :)
Business card, Stationary, Envelopes, Invoice, E-mail signature & Notepad
Check your private massage! thanks!
nice for this time

```html
<!DOCTYPE html>
<html lang="en">
<head>
<meta charset="utf-8">
<title>KV Relay Stationery</title>
<link href="https://fonts.googleapis.com/css2?family=Open+Sans:wght@400;700&display=swap" rel="stylesheet">
<style>
:root{
  --bg:#e9eaec;
  --paper:#ffffff;
  --blue:#1b4fa3;
  --blue-dark:#0c2d73;
  --orange:#f4a11a;
  --ink:#2a3b5c;
  --grey:#7c8593;
  --faint:#eef1f6;
}
*{box-sizing:border-box;margin:0;padding:0}
html,body{width:1200px;height:936px;overflow:hidden}
body{background:var(--bg);position:relative;font-family:"Open Sans",sans-serif;color:var(--ink)}
.sheet{position:absolute;background:var(--paper);box-shadow:0 2px 8px rgba(0,0,0,.12);overflow:hidden}

.brand{display:flex;align-items:center;gap:6px}
.brand-dot{border-radius:50%;background:var(--orange);flex:none}
.brand-name{font-family:"Open Sans",sans-serif;font-weight:700;color:var(--blue);white-space:nowrap;line-height:1}

.footer{position:absolute;left:0;right:0;bottom:0;background:linear-gradient(180deg,var(--blue),var(--blue-dark));display:flex;align-items:center;justify-content:center}
.footer::before{content:"";position:absolute;left:0;right:0;top:-6px;height:3px;background:var(--orange)}
.footer-web{color:#fff;letter-spacing:.35em;font-size:7px}

.contact{font-size:5px;line-height:1.7;color:var(--ink)}
.contact span{display:flex;align-items:center;gap:3px;white-space:nowrap}
.contact i{display:inline-block;width:5px;height:5px;background:var(--blue);border-radius:1px}

/* letterhead */
.letterhead{left:180px;top:71px;width:387px;height:536px}
.letterhead .brand{position:absolute;left:22px;top:26px}
.letterhead .brand-dot{width:12px;height:12px}
.letterhead .brand-name{font-size:13px}
.letterhead .contact{position:absolute;left:292px;top:18px}
.letterhead .watermark{position:absolute;left:0;right:0;top:300px;text-align:center;font-weight:700;font-size:40px;color:var(--faint);line-height:1}
.letterhead .footer{height:30px}

/* folder */
.folder{left:633px;top:71px;width:452px;height:536px}
.folder .brand{position:absolute;left:0;right:0;top:220px;justify-content:center;gap:14px}
.folder .brand-dot{width:40px;height:40px}
.folder .brand-name{font-size:46px}
.folder .footer{height:38px}

/* business cards */
.card-front{left:40px;top:655px;width:200px;height:119px}
.card-front .brand{position:absolute;left:10px;top:12px}
.card-front .brand-dot{width:9px;height:9px}
.card-front .brand-name{font-size:10px}
.card-front .holder{position:absolute;left:10px;top:36px;font-size:6px;font-weight:700;color:var(--blue)}
.card-front .holder small{display:block;font-weight:400;color:var(--grey);font-size:5px}
.card-front .contact{position:absolute;left:118px;top:44px;font-size:4.5px}
.card-front .footer{height:18px}
.card-front .footer-web{font-size:5px}

.card-back{left:40px;top:787px;width:200px;height:114px}
.card-back .center{position:absolute;left:0;right:0;top:34px;display:flex;flex-direction:column;align-items:center;gap:14px}
.card-back .brand-dot{width:10px;height:10px}
.card-back .brand-name{font-size:11px}
.card-back .web{font-size:5px;letter-spacing:.3em;color:var(--grey)}

/* envelopes */
.env-front{left:266px;top:660px;width:346px;height:233px}
.env-front .brand{position:absolute;left:16px;top:16px}
.env-front .brand-dot{width:10px;height:10px}
.env-front .brand-name{font-size:11px}
.env-front .return{position:absolute;left:16px;top:40px;font-size:5px;line-height:1.6;color:var(--grey)}
.env-front .footer{height:40px}

.env-back{left:739px;top:660px;width:420px;height:233px}
.env-back .flap{position:absolute;left:0;top:0;width:420px;height:233px}
.env-back .top-band{position:absolute;left:0;right:0;top:0;height:58px;background:linear-gradient(180deg,var(--blue),var(--blue-dark));display:flex;align-items:center;justify-content:center}
.env-back .top-band::after{content:"";position:absolute;left:0;right:0;bottom:-6px;height:3px;background:var(--orange)}
</style>
</head>
<body>

<section class="sheet letterhead">
  <div class="brand">
    <div class="brand-dot"></div>
    <div class="brand-name">KV Relay</div>
  </div>
  <div class="contact">
    <span><i></i>+62 21 555 0148</span>
    <span><i></i>3F B28 Galeri Nusapark</span>
    <span><i></i>tom@kvrelay.com</span>
    <span><i></i>www.kvrelay.com</span>
  </div>
  <div class="watermark">KV Relay</div>
  <div class="footer"><span class="footer-web">WWW.KVRELAY.COM</span></div>
</section>

<section class="sheet folder">
  <div class="brand">
    <div class="brand-dot"></div>
    <div class="brand-name">KV Relay</div>
  </div>
  <div class="footer"><span class="footer-web">WWW.KVRELAY.COM</span></div>
</section>

<section class="sheet card-front">
  <div class="brand">
    <div class="brand-dot"></div>
    <div class="brand-name">KV Relay</div>
  </div>
  <div class="holder">Tom Variscoff<small>CEO</small></div>
  <div class="contact">
    <span><i></i>+62 21 555 0148</span>
    <span><i></i>tom@kvrelay.com</span>
    <span><i></i>www.kvrelay.com</span>
  </div>
  <div class="footer"><span class="footer-web">WWW.KVRELAY.COM</span></div>
</section>

<section class="sheet card-back">
  <div class="center">
    <div class="brand">
      <div class="brand-dot"></div>
      <div class="brand-name">KV Relay</div>
    </div>
    <div class="web">WWW.KVRELAY.COM</div>
  </div>
</section>

<section class="sheet env-front">
  <div class="brand">
    <div class="brand-dot"></div>
    <div class="brand-name">KV Relay</div>
  </div>
  <div class="return">3F B28 GALERI NUSAPARK<br>JAKARTA PUSAT 14071<br>tom@kvrelay.com</div>
  <div class="footer"><span class="footer-web">WWW.KVRELAY.COM</span></div>
</section>

<section class="sheet env-back">
  <svg class="flap" viewBox="0 0 420 233" aria-hidden="true">
    <polyline points="0,64 210,150 420,64" fill="none" stroke="#e3e6ea" stroke-width="1.5"/>
  </svg>
  <div class="top-band"><span class="footer-web">WWW.KVRELAY.COM</span></div>
</section>

</body>
</html>
```